IT’S NOT A CLEANING, IT’S YOUR LIFE! TOP TEN REASONS WHY THIS IS NOT JUST A “CLEANING”

We made a list for our patients to let them know why our hygiene appointments are different than other cleanings. Since this is a lot of information, we would like it easily readable within 4-5 feet but we do not want the post to be HUGE. Please see below:

IT’S NOT A CLEANING, IT’S YOUR LIFE!
TOP TEN REASONS WHY THIS IS NOT JUST A “CLEANING”

10. We make you look better. Healthy teeth and gums are more attractive. Recent studies
show that the smile is the first thing people notice and that people with better looking teeth
are more confident and successful.

9. We can relieve your headaches. During your hygiene visit we evaluate for serious bite
issues, many of which lead to muscle soreness, headaches, and migraines.

8. We check for oral cancer. Oral cancer kills 1 person per hour 24 hours a day. The death rate for oral cancer is higher than cancers we routinely hear about such as cervical, thyroid and skin cancer.

7. We make you smell better. During your hygiene visit we eliminate many of the germs that live under your gum tissue and cause bad breath.

6. We save you money. By utilizing the latest dental technology (digital x-rays, mouth
cameras, and magnification glasses) we can help with early detection of tooth and gum
problems and save you the cost of gum surgery, root canals, and implants.

5. We clean in places you cannot. We clean under the gum line and between teeth where
most of the germs hide and cause dental disease. 40% of the bacteria in your mouth lives in
between your teeth.

4. We prevent pain. We identify tooth decay that can lead to nerve involvement and pain,
root canal, and tooth loss.

3. We save your teeth. Most tooth loss is from periodontal/gum disease. At each visit we
evaluate the health of your gums and bone with our periodontal screening. Periodontal
disease, like high blood pressure, is symptomless until it is in advanced stages.

2. We protect your loved ones. Studies have proven that the bacteria that cause dental
disease can be transmitted from person to person. Think about that the next time you kiss
someone!

1. We prolong life. Researchers have linked the inflammation and infection found in the
mouth to heart attacks, strokes, and Alzheimer’s. By reducing infection in your mouth we can
greatly improve your overall health!

```html
<!DOCTYPE html>
<html lang="en">
<head>
<meta charset="utf-8">
<title>It’s Not a Cleaning, It’s Your Life!</title>
<link rel="stylesheet" href="https://fonts.googleapis.com/css2?family=Tinos:wght@400;700&display=swap">
<style>
  :root {
    --sky-top: #a9bfe4;
    --sky-bottom: #b8cbea;
    --band: #2c6bd8;
    --heading: #ffffff;
    --heading-shadow: rgba(20, 40, 90, 0.55);
    --body-text: #111111;
    --mascot-tone: #f3f5fa;
    --smile-red: #e0282a;
    --smile-light: #f4d9dc;
  }
  html, body {
    margin: 0;
    padding: 0;
    overflow: hidden;
  }
  .poster {
    position: relative;
    width: 900px;
    height: 1200px;
    overflow: hidden;
    background: linear-gradient(180deg, var(--sky-top) 0%, var(--sky-bottom) 100%);
    font-family: "Tinos", "Times New Roman", serif;
  }
  .header-band {
    position: absolute;
    left: 0;
    top: 0;
    width: 900px;
    height: 300px;
  }
  .header-band .band-shape { fill: var(--band); }
  .header-band .headline {
    font-family: "Tinos", "Times New Roman", serif;
    font-weight: 700;
    fill: var(--heading);
    filter: drop-shadow(2px 3px 2px var(--heading-shadow));
  }
  .smile-art {
    position: absolute;
    left: 660px;
    top: 95px;
    width: 220px;
    height: 140px;
    border-radius: 18px;
    background: radial-gradient(ellipse at 50% 55%, var(--smile-red) 0%, var(--smile-light) 55%, rgba(244, 217, 220, 0) 80%);
    opacity: 0.75;
  }
  .reasons {
    list-style: none;
    margin: 0;
    padding: 0;
  }
  .reason {
    position: absolute;
    left: 0;
    width: 900px;
  }
  .reason .mascot {
    position: absolute;
    left: 6px;
    top: 4px;
    width: 58px;
    height: 52px;
    border-radius: 45% 45% 40% 40%;
    background: var(--mascot-tone);
  }
  .reason .reason-text {
    position: absolute;
    left: 75px;
    top: 0;
    margin: 0;
    font-size: 20.5px;
    line-height: 25px;
    color: var(--body-text);
    white-space: pre;
  }
</style>
</head>
<body>
<main class="poster">
  <svg class="header-band" viewBox="0 0 900 300" xmlns="http://www.w3.org/2000/svg">
    <polygon class="band-shape" points="0,95 900,-25 900,150 0,272"/>
    <text class="headline" x="48" y="148" font-size="33" transform="rotate(-7.5 48 148)">IT’S NOT A CLEANING, IT’S YOUR LIFE!</text>
    <text class="headline" x="8" y="222" font-size="32" transform="rotate(-9.5 8 222)">TOP TEN REASONS WHY THIS IS NOT JUST A “CLEANING”</text>
  </svg>
  <div class="smile-art" role="img" aria-label="Illustration of a smile with a red curved arrow"></div>

  <ol class="reasons">
    <li class="reason" style="top:294px">
      <span class="mascot" role="img" aria-label="Cartoon tooth mascot"></span>
      <p class="reason-text"> We make you look better. Healthy teeth and gums are more attractive. Recent studies
show that the smile is the first thing people notice and that people with better looking teeth
are more confident and successful.</p>
    </li>
    <li class="reason" style="top:394px">
      <span class="mascot" role="img" aria-label="Cartoon tooth mascot"></span>
      <p class="reason-text"> We can relieve your headaches. During your hygiene visit we evaluate for serious bite
issues, many of which lead to muscle soreness, headaches, and migraines.</p>
    </li>
    <li class="reason" style="top:468px">
      <span class="mascot" role="img" aria-label="Cartoon tooth mascot"></span>
      <p class="reason-text">We check for oral cancer. Oral cancer kills 1 person per hour 24 hours a day. The death rate for oral
cancer is higher than cancers we routinely hear about such as cervical, thyroid and skin cancer.</p>
    </li>
    <li class="reason" style="top:543px">
      <span class="mascot" role="img" aria-label="Cartoon tooth mascot"></span>
      <p class="reason-text">We make you smell better. During your hygiene visit we eliminate many of the germs
 that live under your gum tissue and cause bad breath.</p>
    </li>
    <li class="reason" style="top:619px">
      <span class="mascot" role="img" aria-label="Cartoon tooth mascot"></span>
      <p class="reason-text">We save you money. By utilizing the latest dental technology (digital x-rays, mouth
cameras, and magnification glasses) we can help with early detection of tooth and gum
problems and save you the cost of gum surgery, root canals, and implants.</p>
    </li>
    <li class="reason" style="top:718px">
      <span class="mascot" role="img" aria-label="Cartoon tooth mascot"></span>
      <p class="reason-text">We clean in places you cannot. We clean under the gum line and between teeth where
most of the germs hide and cause dental disease. 40% of the bacteria in your mouth lives in
between your teeth.</p>
    </li>
    <li class="reason" style="top:818px">
      <span class="mascot" role="img" aria-label="Cartoon tooth mascot"></span>
      <p class="reason-text">We prevent pain. We identify tooth decay that can lead to nerve involvement and pain,
root canal, and tooth loss.</p>
    </li>
    <li class="reason" style="top:893px">
      <span class="mascot" role="img" aria-label="Cartoon tooth mascot"></span>
      <p class="reason-text">We save your teeth. Most tooth loss is from periodontal/gum disease. At each visit we
evaluate the health of your gums and bone with our periodontal screening. Periodontal
disease, like high blood pressure, is symptomless until it is in advanced stages.</p>
    </li>
    <li class="reason" style="top:993px">
      <span class="mascot" role="img" aria-label="Cartoon tooth mascot"></span>
      <p class="reason-text">We protect your loved ones. Studies have proven that the bacteria that cause dental
disease can be transmitted from person to person. Think about that the next time you kiss
someone!</p>
    </li>
    <li class="reason" style="top:1093px">
      <span class="mascot" role="img" aria-label="Cartoon tooth mascot"></span>
      <p class="reason-text">We prolong life. Researchers have linked the inflammation and infection found in the
mouth to heart attacks, strokes, and Alzheimer’s. By reducing infection in your mouth we can
greatly improve your overall health!</p>
    </li>
  </ol>
</main>
</body>
</html>
```